Powerpoint design for european B2B business

We need a Powerpoint design for a newly established IT company with a B2B focus. We want to develop management information systems that help managers communicate goals into their organization and analyze their organizational activities and performance.

We defined the attached color scale, please relate your design to these colors.

The design should be simple and straight, serious and professional and leave enough space for the content ... :-)

Target Market(s)

B2B, companies larger than 200 employees

Industry/Entity Type

Business

Font styles to use
Sans Serif

Requirements
Should not have
• too playful design, clipart style

```html
<!DOCTYPE html>
<html lang="en">
<head>
<meta charset="utf-8">
<title>Kestrel — Business Insight Software presentation</title>
<link href="https://fonts.googleapis.com/css2?family=Open+Sans:wght@300;400;600;700&display=swap" rel="stylesheet">
<style>
:root{
  --navy:#2e4b6c;--navy-d:#213a56;--green:#8cc09c;--red:#c43d4e;--yellow:#ded45c;
  --sky:#b6cde0;--ink:#34465b;--grey:#7d8a97;--light:#eef2f5;--line:#d6dde4;--white:#fff;
}
*{box-sizing:border-box;margin:0;padding:0}
html,body{width:1200px;height:3148px;overflow:hidden;background:#fff}
body{font-family:"Open Sans",Arial,sans-serif;color:var(--ink)}
.deck{display:grid;grid-template-columns:repeat(3,394px);grid-template-rows:repeat(14,220px);column-gap:9px;row-gap:5.2px;width:1200px;height:3148px}
.slide{position:relative;overflow:hidden;background:var(--white);box-shadow:0 0 0 1px #e3e8ec inset}
.slide.dark{background:var(--navy)}
.a{position:absolute}
.brand{font-weight:600;letter-spacing:.2px;line-height:1}
.logo{position:absolute;top:10px;right:12px;font-weight:600;font-size:12px;color:var(--navy);line-height:1}
.logo.w{color:#fff}
.tag{font-size:4.6px;letter-spacing:1px;color:#fff}
.title{position:absolute;top:12px;left:12px;font-size:13px;font-weight:400;color:var(--navy)}
.title.w{color:#fff}
.rule{position:absolute;top:30px;left:12px;width:54px;height:1px;background:var(--line)}
.foot{position:absolute;left:0;right:0;bottom:0;height:9px;background:var(--navy);display:flex;align-items:center;padding-left:10px;font-size:3.6px;color:#cfd9e3}
.foot b{position:absolute;right:0;top:0;width:12px;height:9px;background:var(--green);color:#fff;font-size:4px;font-weight:600;display:flex;align-items:center;justify-content:center}
.ph{position:absolute;background:linear-gradient(135deg,#a9b9c8,#e0e6ec 55%,#8396a9)}
.ph.cool{background:linear-gradient(160deg,#3d5a7a,#8aa3bb 60%,#cfdbe6)}
.ph.warm{background:linear-gradient(135deg,#c9a27a,#e8d7c0 50%,#8a7f78)}
.ph.night{background:linear-gradient(150deg,#1e2d3e,#3e5168 60%,#1a2634)}
.ph.sky{background:linear-gradient(120deg,#d9e6f2,#9cb8d6 50%,#f3f7fb)}
.ph.face{border-radius:50%;background:radial-gradient(circle at 50% 40%,#d7c2ad,#9b8674 70%,#6e5e52)}
.tint{position:absolute;background:rgba(33,58,86,.78)}
.h{font-size:6px;font-weight:700;color:var(--navy);margin-bottom:2px}
.h.w{color:#fff}
.lead{font-size:6.4px;font-weight:700;color:var(--navy);line-height:1.35}
.tx{font-size:4.4px;line-height:1.5;color:var(--grey)}
.tx.w{color:#d7e1ea}
.ico{display:inline-flex;align-items:center;justify-content:center;border-radius:50%;background:var(--navy);flex:none}
.ico::after{content:"";width:38%;height:38%;border:1.2px solid #fff;border-radius:50%}
.ico.g{background:var(--green)}.ico.r{background:var(--red)}.ico.y{background:var(--yellow)}.ico.sq{border-radius:2px}
.row{display:flex;gap:6px;align-items:flex-start}
.item{display:flex;gap:6px;align-items:center;margin-bottom:9px}
.cols{display:flex;gap:10px}
.cols>div{flex:1}
.center{text-align:center}
</style>
</head>
<body>
<main class="deck">

<!-- 1 cover -->
<section class="slide dark">
  <div class="ph cool" style="inset:0" role="img" aria-label="Photo of a glass office building"></div>
  <div class="tint" style="inset:0"></div>
  <div class="a brand" style="left:42px;top:78px;color:#fff;font-size:34px">Kestrel</div>
  <div class="a tag" style="left:44px;top:120px">Business Insight Software</div>
</section>

<!-- 2 title -->
<section class="slide">
  <div class="a brand" style="top:8px;left:0;right:0;text-align:center;font-size:11px;color:var(--navy)">Kestrel</div>
  <div class="ph" style="left:12px;right:12px;top:26px;height:92px" role="img" aria-label="Photo of business people talking by a window"></div>
  <div class="a" style="left:12px;right:12px;top:118px;height:40px;background:var(--navy);color:#fff;text-align:center;padding-top:9px">
    <div style="font-size:13px">Your Title Goes Here</div><div style="font-size:4.5px;color:#c9d6e2">Your subtitle here</div></div>
  <div class="a" style="left:16px;right:16px;top:168px;display:flex;gap:20px;font-size:5px;color:var(--navy)">
    <div class="row" style="align-items:center"><span class="ico sq" style="width:9px;height:9px"></span>Name Surname</div>
    <div class="row" style="align-items:center"><span class="ico sq" style="width:9px;height:9px"></span>Name Surname</div>
    <div class="row" style="align-items:center"><span class="ico sq" style="width:9px;height:9px"></span>Name Surname</div>
    <div style="margin-left:auto;color:var(--grey)">January 1, 2025</div></div>
  <div class="foot" style="height:5px"></div>
</section>

<!-- 3 title alt -->
<section class="slide">
  <div class="a brand" style="left:20px;top:16px;font-size:14px;color:var(--navy)">Kestrel</div>
  <div class="a tag" style="left:20px;top:33px;color:var(--grey);font-size:3.8px">Business Insight Software</div>
  <div class="ph" style="left:150px;right:12px;top:8px;height:120px" role="img" aria-label="Photo of business people shaking hands"></div>
  <div class="a" style="left:12px;right:12px;top:128px;height:40px;background:var(--navy);color:#fff;text-align:center;padding-top:9px">
    <div style="font-size:13px">Your Title Goes Here</div><div style="font-size:4.5px;color:#c9d6e2">Your subtitle here</div></div>
  <div class="a" style="left:16px;right:16px;top:178px;display:flex;gap:20px;font-size:5px;color:var(--navy)">
    <span>Name Surname</span><span>Name Surname</span><span>Name Surname</span><span style="margin-left:auto;color:var(--grey)">January 1, 2025</span></div>
  <div class="foot" style="height:5px"></div>
</section>

<!-- 4 quote -->
<section class="slide dark">
  <div class="ph night" style="inset:0" role="img" aria-label="Photo of a modern building facade"></div>
  <div class="tint" style="inset:0"></div>
  <div class="a" style="left:183px;top:34px;width:28px;height:28px;border-radius:50%;background:var(--green);color:#fff;font-size:20px;font-weight:700;text-align:center;line-height:34px">“</div>
  <div class="a center" style="left:60px;right:60px;top:78px;color:#fff;font-size:8.5px;line-height:1.45;font-weight:300">Coming together is a beginning;<br>Keeping together is progress;<br>Working together is success.</div>
  <div class="a center" style="left:0;right:0;top:124px;color:#c9d6e2;font-size:4.5px">Quote Author</div>
</section>

<!-- 5 agenda -->
<section class="slide dark">
  <div class="title w">Our Agenda</div><div class="logo w">Kestrel</div>
  <div class="a" style="left:24px;right:24px;top:46px;display:grid;grid-template-columns:1fr 1fr;row-gap:14px;column-gap:30px">
    <div class="item"><span class="ico sq g" style="width:12px;height:12px"></span><div><div class="h w">Agenda One</div><div class="tx w">Short line of agenda text</div></div></div>
    <div class="item"><span class="ico sq g" style="width:12px;height:12px"></span><div><div class="h w">Agenda Four</div><div class="tx w">Short line of agenda text</div></div></div>
    <div class="item"><span class="ico sq g" style="width:12px;height:12px"></span><div><div class="h w">Agenda Two</div><div class="tx w">Short line of agenda text</div></div></div>
    <div class="item"><span class="ico sq g" style="width:12px;height:12px"></span><div><div class="h w">Agenda Five</div><div class="tx w">Short line of agenda text</div></div></div>
    <div class="item"><span class="ico sq g" style="width:12px;height:12px"></span><div><div class="h w">Agenda Three</div><div class="tx w">Short line of agenda text</div></div></div>
    <div class="item"><span class="ico sq g" style="width:12px;height:12px"></span><div><div class="h w">Agenda Six</div><div class="tx w">Short line of agenda text</div></div></div>
  </div>
  <div class="foot"><span>© 2025 Kestrel · Business Insight Software</span><b>5</b></div>
</section>

<!-- 6 about -->
<section class="slide">
  <div class="ph warm" style="inset:0 0 9px 0" role="img" aria-label="Photo of a team smiling in an office"></div>
  <div class="a" style="right:12px;top:64px;width:150px;height:112px;background:var(--navy);padding:12px">
    <div style="color:#fff;font-size:13px;margin-bottom:6px">About Us</div>
    <p class="tx w">We build management information systems that help leaders share goals and measure results.</p>
    <p class="tx w" style="margin-top:4px">Clear reports, simple dashboards and reliable data for every team.</p></div>
  <div class="foot"><span>© 2025 Kestrel · Business Insight Software</span><b>6</b></div>
</section>

<!-- 7 services -->
<section class="slide">
  <div class="title">Our Services</div><div class="rule"></div><div class="logo">Kestrel</div>
  <div class="ph" style="left:12px;top:40px;width:150px;height:80px" role="img" aria-label="Photo of a smiling businessman"></div>
  <div class="a" style="left:12px;top:128px;width:150px"><div class="h">Your Title Goes Here</div><p class="tx">Lorem ipsum dolor sit amet, consectetur adipiscing elit. Sed do eiusmod tempor incididunt ut labore et dolore magna.</p></div>
  <div class="a" style="left:186px;top:48px;width:190px">
    <div class="item"><span class="ico" style="width:16px;height:16px"></span><div><div class="h">Service Number One</div><div class="tx">Lorem ipsum dolor sit amet, consectetur elit.</div></div></div>
    <div class="item"><span class="ico" style="width:16px;height:16px"></span><div><div class="h">Service Number Two</div><div class="tx">Lorem ipsum dolor sit amet, consectetur elit.</div></div></div>
    <div class="item"><span class="ico" style="width:16px;height:16px"></span><div><div class="h">Service Number Three</div><div class="tx">Lorem ipsum dolor sit amet, consectetur elit.</div></div></div>
  </div>
  <div class="foot"><span>© 2025 Kestrel · Business Insight Software</span><b>7</b></div>
</section>

<!-- 8 quote area -->
<section class="slide">
  <div class="title">Quote Area</div><div class="rule"></div><div class="logo">Kestrel</div>
  <div class="a" style="left:12px;top:40px;width:180px;height:124px;background:var(--navy);padding:16px 14px">
    <div style="color:var(--green);font-size:14px;font-weight:700;line-height:.6">“</div>
    <div style="color:#fff;font-size:6.6px;line-height:1.5;margin-top:4px">Coming together is a beginning; keeping together is progress; working together is success.</div>
    <div class="tx w" style="margin-top:8px">— Quote Author</div></div>
  <div class="ph sky" style="left:192px;right:12px;top:40px;height:124px" role="img" aria-label="Photo of abstract blue light streaks"></div>
  <div class="foot"><span>© 2025 Kestrel · Business Insight Software</span><b>8</b></div>
</section>

<!-- 9 text area -->
<section class="slide">
  <div class="title">Text Area</div><div class="rule"></div><div class="logo">Kestrel</div>
  <div class="a" style="left:12px;right:20px;top:48px">
    <p class="lead">This is place for your header text. Insert your text here, just replace this text with your own text</p>
    <p class="tx" style="margin-top:8px">Lorem ipsum dolor sit amet, consectetur adipiscing elit. Sed do eiusmod tempor incididunt ut labore et dolore magna aliqua. Ut enim ad minim veniam, quis nostrud exercitation ullamco laboris nisi ut aliquip ex ea commodo consequat.</p>
    <p class="tx" style="margin-top:6px">Duis aute irure dolor in reprehenderit in voluptate velit esse cillum dolore eu fugiat nulla pariatur. Excepteur sint occaecat cupidatat non proident, sunt in culpa qui officia deserunt mollit anim.</p>
    <p class="tx" style="margin-top:6px">Ut enim ad minim veniam, quis nostrud exercitation ullamco laboris nisi ut aliquip ex ea commodo.</p></div>
  <div class="foot"><span>© 2025 Kestrel · Business Insight Software</span><b>9</b></div>
</section>

<!-- 10 vision mission -->
<section class="slide">
  <div class="title">Our Vision &amp; Mission</div><div class="logo">Kestrel</div>
  <div class="a" style="left:12px;right:12px;top:38px;height:166px;background:var(--navy);padding:18px 16px;display:flex;gap:20px">
    <div style="flex:1"><div style="color:#fff;font-size:10px;margin-bottom:6px">Our Vision</div>
      <div style="color:#fff;font-size:6.6px;font-weight:600;line-height:1.35;margin-bottom:8px">The Better Road to an End<br>Without Better Foundation</div>
      <p class="tx w">Lorem ipsum dolor sit amet, consectetur adipiscing elit, sed do eiusmod tempor incididunt ut labore.</p>
      <p class="tx w" style="margin-top:4px">Ut enim ad minim veniam, quis nostrud exercitation ullamco laboris.</p></div>
    <div style="flex:1"><div style="color:#fff;font-size:10px;margin-bottom:8px">Our Mission</div>
      <div class="item"><span class="ico g" style="width:13px;height:13px"></span><div><div class="h w">First Mission</div><div class="tx w">Lorem ipsum dolor sit amet, consectetur.</div></div></div>
      <div class="item"><span class="ico g" style="width:13px;height:13px"></span><div><div class="h w">Second Mission</div><div class="tx w">Lorem ipsum dolor sit amet, consectetur.</div></div></div>
      <div class="item"><span class="ico g" style="width:13px;height:13px"></span><div><div class="h w">Third Mission</div><div class="tx w">Lorem ipsum dolor sit amet, consectetur.</div></div></div></div>
  </div>
  <div class="foot"><span>© 2025 Kestrel · Business Insight Software</span><b>10</b></div>
</section>

<!-- 11 photo + title -->
<section class="slide">
  <div class="ph" style="left:12px;top:8px;width:164px;height:196px" role="img" aria-label="Photo of a bright office corridor"></div>
  <div class="a" style="left:12px;top:104px;width:164px;height:46px;background:rgba(33,58,86,.85);padding:11px 16px">
    <div class="brand" style="color:#fff;font-size:16px">Kestrel</div><div class="tag" style="font-size:3.8px;margin-top:4px">Business Insight Software</div></div>
  <div class="a" style="left:190px;top:40px;width:190px">
    <div style="font-size:12px;color:var(--navy);margin-bottom:10px">Your Title Goes Here</div>
    <div class="item"><span class="ico" style="width:12px;height:12px"></span><div><div class="h">Your Text Here</div><div class="tx">Lorem ipsum dolor sit amet, consectetur elit.</div></div></div>
    <div class="item"><span class="ico" style="width:12px;height:12px"></span><div><div class="h">Your Text Here</div><div class="tx">Lorem ipsum dolor sit amet, consectetur elit.</div></div></div></div>
  <div class="foot"><span>© 2025 Kestrel · Business Insight Software</span><b>11</b></div>
</section>

<!-- 12 tiles -->
<section class="slide">
  <div class="title">Your Title Goes Here</div><div class="rule"></div><div class="logo">Kestrel</div>
  <div class="a" style="left:12px;right:12px;top:40px;height:160px;display:grid;grid-template-columns:1fr 1fr 1fr;grid-template-rows:1fr 1fr;gap:4px">
    <div class="ph night" style="position:relative" role="img" aria-label="Photo of a city street at night"></div>
    <div style="background:var(--navy);padding:8px"><div class="h w">Your Text Here</div><div class="tx w">Lorem ipsum dolor sit amet, consectetur.</div></div>
    <div class="ph" style="position:relative;background:linear-gradient(135deg,#7fa4c4,#d8e3ce)" role="img" aria-label="Photo of a coastal city"></div>
    <div style="background:var(--navy);padding:8px"><div class="h w">Your Text Here</div><div class="tx w">Lorem ipsum dolor sit amet, consectetur.</div></div>
    <div class="ph warm" style="position:relative;background:linear-gradient(135deg,#e1a04a,#f4dca0 60%,#b46a2a)" role="img" aria-label="Photo of a sunlit interior"></div>
    <div style="background:var(--red);padding:8px"><div class="h w">Your Text Here</div><div class="tx w">Lorem ipsum dolor sit amet, consectetur.</div></div>
  </div>
  <div class="foot"><span>© 2025 Kestrel · Business Insight Software</span><b>12</b></div>
</section>

<!-- 13 building + bullets -->
<section class="slide">
  <div class="ph sky" style="left:0;top:0;width:190px;bottom:9px" role="img" aria-label="Photo looking up at glass skyscrapers"></div>
  <div class="a" style="left:190px;right:0;top:0;bottom:9px;background:var(--navy);padding:36px 16px 0 18px">
    <div class="logo w">Kestrel</div>
    <div class="item"><span class="ico g" style="width:11px;height:11px"></span><div><div class="h w">Your Text Here</div><div class="tx w">Lorem ipsum dolor sit amet, consectetur.</div></div></div>
    <div class="item"><span class="ico g" style="width:11px;height:11px"></span><div><div class="h w">Your Text Here</div><div class="tx w">Lorem ipsum dolor sit amet, consectetur.</div></div></div>
    <div class="item"><span class="ico g" style="width:11px;height:11px"></span><div><div class="h w">Your Text Here</div><div class="tx w">Lorem ipsum dolor sit amet, consectetur.</div></div></div>
    <div class="item"><span class="ico g" style="width:11px;height:11px"></span><div><div class="h w">Your Text Here</div><div class="tx w">Lorem ipsum dolor sit amet, consectetur.</div></div></div></div>
  <div class="foot"><span>© 2025 Kestrel · Business Insight Software</span><b>13</b></div>
</section>

<!-- 14 man on phone -->
<section class="slide">
  <div class="a" style="left:0;top:0;width:120px;bottom:9px;background:var(--navy)"></div>
  <div class="ph" style="left:28px;top:22px;width:130px;height:172px;background:linear-gradient(160deg,#5d6c7c,#c7ced6 55%,#3a4552)" role="img" aria-label="Photo of a businessman on a phone call"></div>
  <div class="logo">Kestrel</div>
  <div class="a" style="left:176px;top:40px;width:200px"><div style="font-size:13px;color:var(--navy);line-height:1.2;margin-bottom:8px">Your Title<br>Goes Here</div>
    <p class="tx">Lorem ipsum dolor sit amet, consectetur adipiscing elit, sed do eiusmod tempor incididunt ut labore et dolore magna aliqua.</p>
    <p class="tx" style="margin-top:5px">Ut enim ad minim veniam, quis nostrud exercitation ullamco laboris nisi ut aliquip.</p></div>
  <div class="foot"><span>© 2025 Kestrel · Business Insight Software</span><b>14</b></div>
</section>

<!-- 15 title + photo -->
<section class="slide">
  <div class="title">Your Title Goes Here</div><div class="rule"></div><div class="logo">Kestrel</div>
  <div class="a" style="left:12px;top:46px;width:170px"><p class="lead">This is place for your header text, insert your text here.</p>
    <p class="tx" style="margin-top:8px">Lorem ipsum dolor sit amet, consectetur adipiscing elit, sed do eiusmod tempor incididunt ut labore et dolore.</p>
    <p class="tx" style="margin-top:5px">Ut enim ad minim veniam, quis nostrud exercitation ullamco laboris nisi ut aliquip ex ea.</p></div>
  <div class="ph warm" style="left:196px;right:12px;top:46px;height:130px" role="img" aria-label="Photo of two colleagues with a tablet"></div>
  <div class="foot"><span>© 2025 Kestrel · Business Insight Software</span><b>15</b></div>
</section>

<!-- 16 two column -->
<section class="slide">
  <div class="title">Two Column Description</div><div class="rule"></div><div class="logo">Kestrel</div>
  <div class="a" style="left:12px;right:20px;top:48px"><p class="lead">This is place for your header text. Insert your text here, just replace this text with your own text</p>
    <div class="cols" style="margin-top:10px;gap:16px">
      <div><p class="tx">Lorem ipsum dolor sit amet, consectetur adipiscing elit, sed do eiusmod tempor incididunt ut labore et dolore magna aliqua. Ut enim ad minim veniam, quis nostrud exercitation.</p><p class="tx" style="margin-top:5px">Duis aute irure dolor in reprehenderit in voluptate velit esse cillum dolore eu fugiat nulla pariatur.</p></div>
      <div><p class="tx">Lorem ipsum dolor sit amet, consectetur adipiscing elit, sed do eiusmod tempor incididunt ut labore et dolore magna aliqua. Ut enim ad minim veniam, quis nostrud exercitation.</p><p class="tx" style="margin-top:5px">Duis aute irure dolor in reprehenderit in voluptate velit esse cillum dolore eu fugiat nulla pariatur.</p></div></div></div>
  <div class="foot"><span>© 2025 Kestrel · Business Insight Software</span><b>16</b></div>
</section>

<!-- 17 coffee break -->
<section class="slide dark">
  <div class="ph night" style="inset:0" role="img" aria-label="Photo of a coffee cup on a dark table"></div>
  <div class="logo w">Kestrel</div>
  <div class="a" style="left:18px;top:150px;color:#fff;font-size:11px;font-weight:600;letter-spacing:.5px">COFFEE BREAK</div>
  <div class="a tx w" style="left:18px;top:166px">Back in fifteen minutes</div>
</section>

<!-- 18 three column -->
<section class="slide">
  <div class="title">Three Column Description</div><div class="rule"></div><div class="logo">Kestrel</div>
  <div class="a" style="left:12px;right:20px;top:48px"><p class="lead">This is place for your header text. Insert your text here, just replace this text with your own text</p>
    <div class="cols" style="margin-top:10px">
      <div><p class="tx">Lorem ipsum dolor sit amet, consectetur adipiscing elit, sed do eiusmod tempor incididunt ut labore et dolore.</p><p class="tx" style="margin-top:5px">Duis aute irure dolor in reprehenderit in voluptate velit esse.</p></div>
      <div><p class="tx">Lorem ipsum dolor sit amet, consectetur adipiscing elit, sed do eiusmod tempor incididunt ut labore et dolore.</p><p class="tx" style="margin-top:5px">Duis aute irure dolor in reprehenderit in voluptate velit esse.</p></div>
      <div><p class="tx">Lorem ipsum dolor sit amet, consectetur adipiscing elit, sed do eiusmod tempor incididunt ut labore et dolore.</p><p class="tx" style="margin-top:5px">Duis aute irure dolor in reprehenderit in voluptate velit esse.</p></div></div></div>
  <div class="foot"><span>© 2025 Kestrel · Business Insight Software</span><b>18</b></div>
</section>

<!-- 19 building section -->
<section class="slide dark">
  <div class="ph" style="inset:0;background:linear-gradient(135deg,#39495b,#c7d0d9 50%,#2b3744)" role="img" aria-label="Photo of a steel and glass roof structure"></div>
  <div class="tint" style="left:120px;top:0;width:140px;bottom:0"></div>
  <div class="a center brand" style="left:120px;width:140px;top:32px;color:#fff;font-size:16px">Kestrel</div>
  <div class="a" style="left:140px;width:100px;top:68px;display:flex;justify-content:space-between">
    <span class="ico g" style="width:14px;height:14px"></span><span class="ico g" style="width:14px;height:14px"></span><span class="ico g" style="width:14px;height:14px"></span></div>
  <div class="a center" style="left:120px;width:140px;top:130px;color:#fff;font-size:10px">Your Title Goes Here</div>
  <div class="a center tx w" style="left:120px;width:140px;top:146px">Your subtitle here</div>
  <div class="a" style="left:120px;width:140px;top:196px;height:14px;background:var(--green)"></div>
</section>

<!-- 20 numbered -->
<section class="slide">
  <div class="title">Your Title Goes Here</div><div class="rule"></div><div class="logo">Kestrel</div>
  <div class="a" style="left:12px;top:40px;width:170px"><div class="h" style="margin-bottom:8px">Heading Goes Here</div>
    <div class="item"><span class="ico g" style="width:13px;height:13px"></span><div><div class="h">Service Number One</div><div class="tx">Lorem ipsum dolor sit amet.</div></div></div>
    <div class="item"><span class="ico y" style="width:13px;height:13px"></span><div><div class="h">Service Number Two</div><div class="tx">Lorem ipsum dolor sit amet.</div></div></div>
    <div class="item"><span class="ico r" style="width:13px;height:13px"></span><div><div class="h">Service Number Three</div><div class="tx">Lorem ipsum dolor sit amet.</div></div></div></div>
  <div class="a" style="left:196px;right:12px;top:48px">
    <div style="display:flex;height:30px;margin-bottom:6px"><div style="width:28px;background:var(--navy);color:#fff;font-size:14px;font-weight:700;text-align:center;line-height:30px">1</div><div style="flex:1;background:var(--light);padding:6px"><div class="tx">Lorem ipsum dolor sit amet, consectetur adipiscing elit sed do eiusmod.</div></div></div>
    <div style="display:flex;height:30px;margin-bottom:6px"><div style="width:28px;background:var(--navy);color:#fff;font-size:14px;font-weight:700;text-align:center;line-height:30px">2</div><div style="flex:1;background:var(--light);padding:6px"><div class="tx">Lorem ipsum dolor sit amet, consectetur adipiscing elit sed do eiusmod.</div></div></div>
    <div style="display:flex;height:30px"><div style="width:28px;background:var(--red);color:#fff;font-size:14px;font-weight:700;text-align:center;line-height:30px">3</div><div style="flex:1;background:var(--light);padding:6px"><div class="tx">Lorem ipsum dolor sit amet, consectetur adipiscing elit sed do eiusmod.</div></div></div></div>
  <div class="foot"><span>© 2025 Kestrel · Business Insight Software</span><b>20</b></div>
</section>

<!-- 21 title + two photos -->
<section class="slide">
  <div class="logo">Kestrel</div>
  <div class="a" style="left:12px;top:30px;width:110px"><div style="font-size:12px;color:var(--navy);line-height:1.2;margin-bottom:8px">Your Title<br>Goes Here</div>
    <p class="tx">Lorem ipsum dolor sit amet, consectetur adipiscing elit, sed do eiusmod tempor incididunt ut labore.</p>
    <p class="tx" style="margin-top:5px">Ut enim ad minim veniam, quis nostrud exercitation.</p></div>
  <div class="ph" style="left:136px;right:12px;top:30px;height:84px;background:linear-gradient(135deg,#c6ccd2,#f2f4f6 60%,#8e99a4)" role="img" aria-label="Photo of hands reviewing printed reports"></div>
  <div class="ph" style="left:136px;right:12px;top:118px;height:84px;background:linear-gradient(135deg,#5c6e80,#b9c6d2 60%,#e8edf1)" role="img" aria-label="Photo of a laptop on a desk"></div>
  <div class="foot"><span>© 2025 Kestrel · Business Insight Software</span><b>21</b></div>
</section>

<!-- 22 your title -->
<section class="slide">
  <div class="title">Your Title</div><div class="rule"></div><div class="logo">Kestrel</div>
  <div class="ph" style="left:12px;top:38px;width:110px;height:60px" role="img" aria-label="Photo of two business people standing"></div>
  <div class="ph sky" style="left:126px;top:38px;width:110px;height:60px" role="img" aria-label="Photo of a desk with charts and a pen"></div>
  <div class="a" style="left:12px;top:106px;width:224px"><div class="h">Heading Goes Here</div><p class="tx">Lorem ipsum dolor sit amet, consectetur adipiscing elit, sed do eiusmod tempor incididunt ut labore et dolore magna aliqua. Ut enim ad minim veniam.</p></div>
  <div class="a" style="left:250px;top:46px;width:130px">
    <div class="item"><span class="ico" style="width:11px;height:11px"></span><div><div class="h">Your Text Here</div><div class="tx">Lorem ipsum dolor sit.</div></div></div>
    <div class="item"><span class="ico" style="width:11px;height:11px"></span><div><div class="h">Your Text Here</div><div class="tx">Lorem ipsum dolor sit.</div></div></div>
    <div class="item"><span class="ico" style="width:11px;height:11px"></span><div><div class="h">Your Text Here</div><div class="tx">Lorem ipsum dolor sit.</div></div></div>
    <div class="item"><span class="ico" style="width:11px;height:11px"></span><div><div class="h">Your Text Here</div><div class="tx">Lorem ipsum dolor sit.</div></div></div></div>
  <div class="foot"><span>© 2025 Kestrel · Business Insight Software</span><b>22</b></div>
</section>

<!-- 23 pictures with bullets -->
<section class="slide">
  <div class="title">Pictures with Bullets</div><div class="rule"></div><div class="logo">Kestrel</div>
  <div class="a" style="left:56px;right:56px;top:42px;height:46px;display:flex;gap:4px">
    <div class="ph" style="position:relative;flex:1" role="img" aria-label="Photo of a meeting table"></div>
    <div class="ph sky" style="position:relative;flex:1" role="img" aria-label="Photo of a laptop screen"></div>
    <div class="ph" style="position:relative;flex:1;background:linear-gradient(135deg,#4b6786,#cbd7e2)" role="img" aria-label="Photo of a city skyline"></div></div>
  <div class="a" style="left:56px;right:56px;top:104px;display:flex;gap:20px">
    <div style="flex:1"><div class="h">Heading Goes Here</div><p class="tx">Lorem ipsum dolor sit amet, consectetur adipiscing elit, sed do eiusmod tempor incididunt ut labore.</p></div>
    <div style="flex:1"><div class="h">Heading Goes Here</div><p class="tx">Lorem ipsum dolor sit amet, consectetur adipiscing elit, sed do eiusmod tempor incididunt ut labore.</p></div></div>
  <div class="foot"><span>© 2025 Kestrel · Business Insight Software</span><b>23</b></div>
</section>

<!-- 24 section -->
<section class="slide dark">
  <div class="a brand" style="left:130px;top:56px;color:#fff;font-size:24px">Kestrel</div>
  <div class="a tag" style="left:132px;top:86px;font-size:4px">Business Insight Software</div>
  <div class="a center" style="left:0;right:0;top:124px;color:#fff;font-size:11px">Your Title Goes Here</div>
  <div class="a center tx w" style="left:0;right:0;top:140px">Your subtitle here</div>
</section>

<!-- 25 paragraph three bullet -->
<section class="slide">
  <div class="title">Paragraph with Three Bullet</div><div class="rule"></div><div class="logo">Kestrel</div>
  <div class="a" style="left:12px;top:44px;width:120px"><p class="lead">This is place for your header text. Insert your text here, just replace this text with your own text</p>
    <p class="tx" style="margin-top:6px">Lorem ipsum dolor sit amet, consectetur adipiscing elit, sed do eiusmod tempor incididunt ut labore et dolore magna aliqua.</p>
    <p class="tx" style="margin-top:5px">Ut enim ad minim veniam, quis nostrud exercitation ullamco.</p></div>
  <div class="a" style="left:146px;right:12px;top:74px;display:flex;gap:8px">
    <div class="center" style="flex:1"><span class="ico" style="width:18px;height:18px;background:#fff;border:1px solid var(--navy)"></span><div class="h" style="margin-top:5px">Your Text Here</div><div class="tx">Lorem ipsum dolor sit amet, consectetur adipiscing.</div></div>
    <div class="center" style="flex:1"><span class="ico" style="width:18px;height:18px;background:#fff;border:1px solid var(--navy)"></span><div class="h" style="margin-top:5px">Your Text Here</div><div class="tx">Lorem ipsum dolor sit amet, consectetur adipiscing.</div></div>
    <div class="center" style="flex:1"><span class="ico" style="width:18px;height:18px;background:#fff;border:1px solid var(--navy)"></span><div class="h" style="margin-top:5px">Your Text Here</div><div class="tx">Lorem ipsum dolor sit amet, consectetur adipiscing.</div></div></div>
  <div class="foot"><span>© 2025 Kestrel · Business Insight Software</span><b>25</b></div>
</section>

<!-- 26 global experience -->
<section class="slide">
  <div class="title">Global Experience</div><div class="rule"></div><div class="logo">Kestrel</div>
  <div class="a" style="left:20px;right:20px;top:38px;height:142px;background:linear-gradient(180deg,#dfe5eb,#cfd7df);border-radius:3px" role="img" aria-label="World map with office locations"></div>
  <div class="a row" style="left:14px;top:186px;align-items:center"><span class="ico" style="width:9px;height:9px"></span><div><div class="h" style="margin:0">Heading Goes Here</div><div class="tx">Lorem ipsum dolor sit amet.</div></div></div>
  <div class="foot"><span>© 2025 Kestrel · Business Insight Software</span><b>26</b></div>
</section>

<!-- 27 multiple column -->
<section class="slide">
  <div class="title">Multiple Column Area</div><div class="rule"></div><div class="logo">Kestrel</div>
  <div class="a" style="left:12px;right:12px;top:44px;display:flex;gap:6px">
    <div class="center" style="flex:1"><span class="ico" style="width:14px;height:14px"></span><div class="h" style="margin-top:4px">Your Text</div><div class="tx">Lorem ipsum dolor sit amet.</div></div>
    <div class="center" style="flex:1"><span class="ico" style="width:14px;height:14px"></span><div class="h" style="margin-top:4px">Your Text</div><div class="tx">Lorem ipsum dolor sit amet.</div></div>
    <div class="center" style="flex:1"><span class="ico" style="width:14px;height:14px"></span><div class="h" style="margin-top:4px">Your Text</div><div class="tx">Lorem ipsum dolor sit amet.</div></div>
    <div class="center" style="flex:1"><span class="ico" style="width:14px;height:14px"></span><div class="h" style="margin-top:4px">Your Text</div><div class="tx">Lorem ipsum dolor sit amet.</div></div>
    <div class="center" style="flex:1"><span class="ico" style="width:14px;height:14px"></span><div class="h" style="margin-top:4px">Your Text</div><div class="tx">Lorem ipsum dolor sit amet.</div></div></div>
  <div class="a" style="left:12px;right:12px;top:120px;display:flex;gap:16px">
    <div style="flex:1"><div style="font-size:8px;color:var(--navy);margin-bottom:3px">Heading Goes Here</div><p class="tx">Lorem ipsum dolor sit amet, consectetur adipiscing elit, sed do eiusmod tempor incididunt ut labore et dolore.</p></div>
    <div style="flex:1"><div style="font-size:8px;color:var(--navy);margin-bottom:3px">Heading Goes Here</div><p class="tx">Lorem ipsum dolor sit amet, consectetur adipiscing elit, sed do eiusmod tempor incididunt ut labore et dolore.</p></div></div>
  <div class="foot"><span>© 2025 Kestrel · Business Insight Software</span><b>27</b></div>
</section>

<!-- 28 brand panel + bullets -->
<section class="slide">
  <div class="a" style="left:0;top:0;width:150px;bottom:9px;background:var(--navy)"></div>
  <div class="a brand" style="left:26px;top:22px;color:#fff;font-size:16px">Kestrel</div>
  <div class="ph sky" style="left:26px;top:56px;width:124px;height:110px" role="img" aria-label="Photo of a man walking in a bright atrium"></div>
  <div class="logo">Kestrel</div>
  <div class="a" style="left:166px;top:36px;width:214px"><div style="font-size:12px;color:var(--navy);margin-bottom:6px">Your Title Goes Here</div>
    <p class="tx">Lorem ipsum dolor sit amet, consectetur adipiscing elit, sed do eiusmod tempor incididunt ut labore et dolore magna.</p>
    <div style="display:grid;grid-template-columns:1fr 1fr;gap:6px 10px;margin-top:12px">
      <div class="row" style="align-items:center"><span class="ico" style="width:11px;height:11px"></span><div><div class="h" style="margin:0">Your Text Here</div><div class="tx">Lorem ipsum dolor.</div></div></div>
      <div class="row" style="align-items:center"><span class="ico" style="width:11px;height:11px"></span><div><div class="h" style="margin:0">Your Text Here</div><div class="tx">Lorem ipsum dolor.</div></div></div>
      <div class="row" style="align-items:center"><span class="ico" style="width:11px;height:11px"></span><div><div class="h" style="margin:0">Your Text Here</div><div class="tx">Lorem ipsum dolor.</div></div></div>
      <div class="row" style="align-items:center"><span class="ico" style="width:11px;height:11px"></span><div><div class="h" style="margin:0">Your Text Here</div><div class="tx">Lorem ipsum dolor.</div></div></div></div></div>
  <div class="foot"><span>© 2025 Kestrel · Business Insight Software</span><b>28</b></div>
</section>

<!-- 29 section photo -->
<section class="slide dark">
  <div class="ph night" style="inset:0" role="img" aria-label="Photo of a building interior"></div>
  <div class="tint" style="inset:0"></div>
  <div class="logo w">Kestrel</div>
  <div class="a center" style="left:0;right:0;top:100px;color:#fff;font-size:13px"><div class="tx w" style="margin-bottom:2px">Section Title</div>Your Title Goes Here</div>
  <div class="a center tx w" style="left:0;right:0;top:126px">Your subtitle here</div>
</section>

<!-- 30 video -->
<section class="slide">
  <div class="logo">Kestrel</div>
  <div class="a" style="left:12px;top:40px;width:110px"><div style="font-size:12px;color:var(--navy);line-height:1.2;margin-bottom:8px">Video Title<br>Goes Here</div>
    <p class="tx">Lorem ipsum dolor sit amet, consectetur adipiscing elit, sed do eiusmod tempor incididunt.</p>
    <p class="tx" style="margin-top:5px">Ut enim ad minim veniam, quis nostrud exercitation ullamco.</p></div>
  <div class="a" style="left:150px;right:16px;top:34px;height:126px;background:#1e2933;padding:4px;border-radius:3px" role="img" aria-label="Video player in a desktop monitor">
    <div style="width:100%;height:100%;background:linear-gradient(135deg,#dfe7ee,#9fb6cb)"></div></div>
  <div class="a" style="left:246px;top:160px;width:36px;height:16px;background:#c3cbd2"></div>
  <div class="a" style="left:230px;top:176px;width:68px;height:3px;background:#c3cbd2"></div>
  <div class="foot"><span>© 2025 Kestrel · Business Insight Software</span><b>30</b></div>
</section>

<!-- 31 four column boxes -->
<section class="slide">
  <div class="title">Four Column Area</div><div class="rule"></div><div class="logo">Kestrel</div>
  <div class="a" style="left:24px;right:24px;top:58px;height:106px;display:flex;gap:10px">
    <div class="center" style="flex:1;background:var(--navy);padding-top:14px"><span class="ico" style="width:18px;height:18px;background:#fff;opacity:.9"></span><div class="h w" style="margin-top:10px">Your Text</div><div class="tx w" style="padding:0 6px">Lorem ipsum dolor sit amet.</div></div>
    <div class="center" style="flex:1;background:var(--green);padding-top:14px"><span class="ico" style="width:18px;height:18px;background:#fff;opacity:.9"></span><div class="h w" style="margin-top:10px">Your Text</div><div class="tx w" style="padding:0 6px">Lorem ipsum dolor sit amet.</div></div>
    <div class="center" style="flex:1;background:var(--red);padding-top:14px"><span class="ico" style="width:18px;height:18px;background:#fff;opacity:.9"></span><div class="h w" style="margin-top:10px">Your Text</div><div class="tx w" style="padding:0 6px">Lorem ipsum dolor sit amet.</div></div>
    <div class="center" style="flex:1;background:var(--yellow);padding-top:14px"><span class="ico" style="width:18px;height:18px;background:#fff;opacity:.9"></span><div class="h w" style="margin-top:10px">Your Text</div><div class="tx w" style="padding:0 6px">Lorem ipsum dolor sit amet.</div></div></div>
  <div class="foot"><span>© 2025 Kestrel · Business Insight Software</span><b>31</b></div>
</section>

<!-- 32 four column rings -->
<section class="slide">
  <div class="title">Four Column Area</div><div class="rule"></div><div class="logo">Kestrel</div>
  <div class="a" style="left:20px;right:20px;top:48px;display:flex;gap:10px">
    <div class="center" style="flex:1"><div style="width:50px;height:50px;margin:0 auto;border-radius:50%;border:4px solid var(--navy);display:flex;align-items:center;justify-content:center"><span class="ico" style="width:18px;height:18px"></span></div><div class="h" style="margin-top:8px">COLUMN 1</div><div class="tx">Lorem ipsum dolor sit amet, consectetur.</div></div>
    <div class="center" style="flex:1"><div style="width:50px;height:50px;margin:0 auto;border-radius:50%;border:4px solid var(--green);display:flex;align-items:center;justify-content:center"><span class="ico g" style="width:18px;height:18px"></span></div><div class="h" style="margin-top:8px">COLUMN 2</div><div class="tx">Lorem ipsum dolor sit amet, consectetur.</div></div>
    <div class="center" style="flex:1"><div style="width:50px;height:50px;margin:0 auto;border-radius:50%;border:4px solid var(--red);display:flex;align-items:center;justify-content:center"><span class="ico r" style="width:18px;height:18px"></span></div><div class="h" style="margin-top:8px">COLUMN 3</div><div class="tx">Lorem ipsum dolor sit amet, consectetur.</div></div>
    <div class="center" style="flex:1"><div style="width:50px;height:50px;margin:0 auto;border-radius:50%;border:4px solid var(--yellow);display:flex;align-items:center;justify-content:center"><span class="ico y" style="width:18px;height:18px"></span></div><div class="h" style="margin-top:8px">COLUMN 4</div><div class="tx">Lorem ipsum dolor sit amet, consectetur.</div></div></div>
  <div class="foot"><span>© 2025 Kestrel · Business Insight Software</span><b>32</b></div>
</section>

<!-- 33 key points -->
<section class="slide">
  <div class="title">Key Points Area</div><div class="rule"></div><div class="logo">Kestrel</div>
  <p class="a tx" style="left:40px;right:40px;top:42px;text-align:center">Lorem ipsum dolor sit amet, consectetur adipiscing elit, sed do eiusmod tempor incididunt ut labore et dolore magna aliqua.</p>
  <svg class="a" style="left:67px;top:70px" width="260" height="60" viewBox="0 0 260 60">
    <g opacity=".92"><circle cx="30" cy="30" r="29" fill="#2e4b6c"/><circle cx="80" cy="30" r="29" fill="#8cc09c"/><circle cx="130" cy="30" r="29" fill="#c43d4e"/><circle cx="180" cy="30" r="29" fill="#8cc09c"/><circle cx="230" cy="30" r="29" fill="#2e4b6c"/></g>
    <g fill="none" stroke="#fff" stroke-width="1.5"><circle cx="30" cy="24" r="5"/><circle cx="80" cy="24" r="5"/><circle cx="130" cy="24" r="5"/><circle cx="180" cy="24" r="5"/><circle cx="230" cy="24" r="5"/></g>
    <g fill="#fff" font-family="Open Sans,sans-serif" font-size="5" text-anchor="middle"><text x="30" y="40">Text</text><text x="80" y="40">Text</text><text x="130" y="40">Text</text><text x="180" y="40">Text</text><text x="230" y="40">Text</text></g>
  </svg>
  <p class="a tx" style="left:40px;right:40px;top:146px;text-align:center">Ut enim ad minim veniam, quis nostrud exercitation ullamco laboris nisi ut aliquip ex ea commodo consequat. Duis aute irure dolor in reprehenderit.</p>
  <div class="foot"><span>© 2025 Kestrel · Business Insight Software</span><b>33</b></div>
</section>

<!-- 34 workflow -->
<section class="slide">
  <div class="title">Workflow Area</div><div class="rule"></div><div class="logo">Kestrel</div>
  <p class="a tx" style="left:120px;right:60px;top:40px">Lorem ipsum dolor sit amet, consectetur adipiscing elit, sed do eiusmod tempor incididunt ut labore.</p>
  <svg class="a" style="left:12px;top:62px" width="370" height="120" viewBox="0 0 370 120" fill="none" stroke-width="9">
    <path d="M20 90 A42 42 0 0 1 104 90" stroke="#2e4b6c"/>
    <path d="M104 70 A42 42 0 0 0 188 70" stroke="#8cc09c"/>
    <path d="M188 90 A42 42 0 0 1 272 90" stroke="#2e4b6c"/>
    <path d="M272 70 A42 42 0 0 0 356 70" stroke="#8cc09c"/>
    <g fill="#fff" stroke="#2e4b6c" stroke-width="1.5"><circle cx="62" cy="48" r="5"/><circle cx="146" cy="112" r="5"/><circle cx="230" cy="48" r="5"/><circle cx="314" cy="112" r="5"/></g>
    <g font-family="Open Sans,sans-serif" font-size="6" font-weight="700" fill="#2e4b6c" stroke="none" text-anchor="middle"><text x="62" y="80">Step 1</text><text x="146" y="18">Step 2</text><text x="230" y="80">Step 3</text><text x="314" y="18">Step 4</text></g>
  </svg>
  <div class="foot"><span>© 2025 Kestrel · Business Insight Software</span><b>34</b></div>
</section>

<!-- 35 timeline -->
<section class="slide">
  <div class="title">Timeline</div><div class="rule"></div><div class="logo">Kestrel</div>
  <svg class="a" style="left:12px;top:36px" width="370" height="150" viewBox="0 0 370 150">
    <line x1="20" y1="76" x2="350" y2="76" stroke="#d6dde4" stroke-width="2"/>
    <g stroke="#2e4b6c" stroke-width="1"><line x1="40" y1="76" x2="40" y2="60"/><line x1="112" y1="76" x2="112" y2="96"/><line x1="184" y1="76" x2="184" y2="40"/><line x1="256" y1="76" x2="256" y2="96"/><line x1="328" y1="76" x2="328" y2="60"/></g>
    <circle cx="40" cy="48" r="14" fill="#2e4b6c"/><circle cx="112" cy="108" r="14" fill="#ded45c"/><circle cx="184" cy="24" r="18" fill="#8cc09c"/><circle cx="256" cy="108" r="14" fill="#c43d4e"/><circle cx="328" cy="48" r="14" fill="#2e4b6c"/>
    <g fill="#fff" font-family="Open Sans,sans-serif" font-size="6" font-weight="700" text-anchor="middle"><text x="40" y="50">2021</text><text x="112" y="110">2022</text><text x="184" y="26">2023</text><text x="256" y="110">2024</text><text x="328" y="50">2025</text></g>
    <g font-family="Open Sans,sans-serif"><text x="20" y="136" font-size="5.5" font-weight="700" fill="#2e4b6c">Your Text Here</text><text x="20" y="144" font-size="4.4" fill="#7d8a97">Lorem ipsum dolor sit amet.</text>
      <text x="290" y="136" font-size="5.5" font-weight="700" fill="#2e4b6c">Your Text Here</text><text x="290" y="144" font-size="4.4" fill="#7d8a97">Lorem ipsum dolor sit amet.</text></g>
  </svg>
  <div class="foot"><span>© 2025 Kestrel · Business Insight Software</span><b>35</b></div>
</section>

<!-- 36 bar chart -->
<section class="slide">
  <div class="title">Bullet &amp; Chart Area</div><div class="rule"></div><div class="logo">Kestrel</div>
  <svg class="a" style="left:12px;top:44px" width="220" height="140" viewBox="0 0 220 140" font-family="Open Sans,sans-serif" font-size="5" fill="#7d8a97">
    <g stroke="#e3e8ec"><line x1="40" y1="0" x2="40" y2="128"/><line x1="80" y1="0" x2="80" y2="128"/><line x1="120" y1="0" x2="120" y2="128"/><line x1="160" y1="0" x2="160" y2="128"/><line x1="200" y1="0" x2="200" y2="128"/></g>
    <text x="0" y="14">Item 1</text><text x="0" y="46">Item 2</text><text x="0" y="78">Item 3</text><text x="0" y="110">Item 4</text>
    <rect x="40" y="6" width="150" height="5" fill="#2e4b6c"/><rect x="40" y="13" width="110" height="5" fill="#8cc09c"/>
    <rect x="40" y="38" width="120" height="5" fill="#2e4b6c"/><rect x="40" y="45" width="150" height="5" fill="#8cc09c"/>
    <rect x="40" y="70" width="90" height="5" fill="#2e4b6c"/><rect x="40" y="77" width="130" height="5" fill="#8cc09c"/>
    <rect x="40" y="102" width="160" height="5" fill="#2e4b6c"/><rect x="40" y="109" width="70" height="5" fill="#8cc09c"/>
  </svg>
  <div class="a" style="left:254px;top:44px;width:130px">
    <div class="item"><span class="ico" style="width:12px;height:12px"></span><div><div class="h">Category One</div><div class="tx">Lorem ipsum dolor sit.</div></div></div>
    <div class="item"><span class="ico g" style="width:12px;height:12px"></span><div><div class="h">Category Two</div><div class="tx">Lorem ipsum dolor sit.</div></div></div>
    <div class="item"><span class="ico" style="width:12px;height:12px"></span><div><div class="h">Category Three</div><div class="tx">Lorem ipsum dolor sit.</div></div></div>
    <div class="item"><span class="ico g" style="width:12px;height:12px"></span><div><div class="h">Category Four</div><div class="tx">Lorem ipsum dolor sit.</div></div></div></div>
  <div class="foot"><span>© 2025 Kestrel · Business Insight Software</span><b>36</b></div>
</section>

<!-- 37 table -->
<section class="slide">
  <div class="title">Table Area</div><div class="rule"></div><div class="logo">Kestrel</div>
  <svg class="a" style="left:40px;top:40px" width="314" height="156" viewBox="0 0 314 156" font-family="Open Sans,sans-serif" font-size="5">
    <rect x="0" y="6" width="94" height="18" fill="#2e4b6c"/><rect x="94" y="0" width="110" height="24" fill="#c43d4e"/><rect x="204" y="6" width="110" height="18" fill="#8cc09c"/>
    <text x="10" y="18" fill="#fff" font-weight="700">Description</text><text x="149" y="15" fill="#fff" font-weight="700" text-anchor="middle">Standard</text><text x="259" y="18" fill="#fff" font-weight="700" text-anchor="middle">Premium</text>
    <g fill="#f3f6f8"><rect x="0" y="24" width="314" height="16"/><rect x="0" y="56" width="314" height="16"/><rect x="0" y="88" width="314" height="16"/><rect x="0" y="120" width="314" height="16"/></g>
    <g fill="#7d8a97"><text x="10" y="34">Feature 1</text><text x="10" y="50">Feature 2</text><text x="10" y="66">Feature 3</text><text x="10" y="82">Feature 4</text><text x="10" y="98">Feature 5</text><text x="10" y="114">Feature 6</text><text x="10" y="130">Feature 7</text><text x="10" y="146">Feature 8</text></g>
    <g fill="#2e4b6c" text-anchor="middle"><text x="149" y="34">✓</text><text x="149" y="50">✓</text><text x="149" y="66">✓</text><text x="149" y="98">✓</text><text x="149" y="146">Text</text>
      <text x="259" y="34">✓</text><text x="259" y="50">✓</text><text x="259" y="66">✓</text><text x="259" y="82">✓</text><text x="259" y="98">✓</text><text x="259" y="114">✓</text><text x="259" y="146">Text</text></g>
  </svg>
  <div class="foot"><span>© 2025 Kestrel · Business Insight Software</span><b>37</b></div>
</section>

<!-- 38 donut -->
<section class="slide">
  <div class="title">Bullet &amp; Chart Area</div><div class="rule"></div><div class="logo">Kestrel</div>
  <div class="a" style="left:24px;top:44px;width:150px">
    <div class="item"><span class="ico" style="width:12px;height:12px"></span><div><div class="h">Your Text Here</div><div class="tx">Lorem ipsum dolor sit amet.</div></div></div>
    <div class="item"><span class="ico g" style="width:12px;height:12px"></span><div><div class="h">Your Text Here</div><div class="tx">Lorem ipsum dolor sit amet.</div></div></div>
    <div class="item"><span class="ico r" style="width:12px;height:12px"></span><div><div class="h">Your Text Here</div><div class="tx">Lorem ipsum dolor sit amet.</div></div></div>
    <div class="item"><span class="ico y" style="width:12px;height:12px"></span><div><div class="h">Your Text Here</div><div class="tx">Lorem ipsum dolor sit amet.</div></div></div></div>
  <svg class="a" style="left:200px;top:40px" width="180" height="150" viewBox="0 0 180 150" font-family="Open Sans,sans-serif" font-size="8" font-weight="700">
    <g transform="translate(90 75) rotate(-90)" fill="none" stroke-width="16">
      <circle r="50" stroke="#2e4b6c" stroke-dasharray="125.7 314.2"/>
      <circle r="50" stroke="#8cc09c" stroke-dasharray="78.5 314.2" stroke-dashoffset="-125.7"/>
      <circle r="50" stroke="#c43d4e" stroke-dasharray="47.1 314.2" stroke-dashoffset="-204.2"/>
      <circle r="50" stroke="#ded45c" stroke-dasharray="62.9 314.2" stroke-dashoffset="-251.3"/></g>
    <text x="150" y="80" fill="#2e4b6c">40%</text><text x="62" y="142" fill="#8cc09c">25%</text><text x="4" y="70" fill="#c43d4e">15%</text><text x="60" y="14" fill="#c9bf3e">20%</text>
    <g fill="#2e4b6c"><rect x="80" y="72" width="4" height="10"/><rect x="86" y="66" width="4" height="16"/><rect x="92" y="70" width="4" height="12"/></g>
  </svg>
  <div class="foot"><span>© 2025 Kestrel · Business Insight Software</span><b>38</b></div>
</section>

<!-- 39 team -->
<section class="slide">
  <div class="title">Our Team</div><div class="rule"></div><div class="logo">Kestrel</div>
  <div class="a" style="left:20px;right:20px;top:42px;display:grid;grid-template-columns:1fr 1fr;gap:16px 20px">
    <div class="row"><div class="ph face" style="position:relative;width:30px;height:30px;flex:none" role="img" aria-label="Portrait of team member"></div><div><div class="h">Name Surname</div><div class="tx">Position Title</div><div class="tx">Lorem ipsum dolor sit amet, consectetur.</div></div></div>
    <div class="row"><div class="ph face" style="position:relative;width:30px;height:30px;flex:none" role="img" aria-label="Portrait of team member"></div><div><div class="h">Name Surname</div><div class="tx">Position Title</div><div class="tx">Lorem ipsum dolor sit amet, consectetur.</div></div></div>
    <div class="row"><div class="ph face" style="position:relative;width:30px;height:30px;flex:none" role="img" aria-label="Portrait of team member"></div><div><div class="h">Name Surname</div><div class="tx">Position Title</div><div class="tx">Lorem ipsum dolor sit amet, consectetur.</div></div></div>
    <div class="row"><div class="ph face" style="position:relative;width:30px;height:30px;flex:none" role="img" aria-label="Portrait of team member"></div><div><div class="h">Name Surname</div><div class="tx">Position Title</div><div class="tx">Lorem ipsum dolor sit amet, consectetur.</div></div></div></div>
  <div class="foot"><span>© 2025 Kestrel · Business Insight Software</span><b>39</b></div>
</section>

<!-- 40 team columns -->
<section class="slide">
  <div class="title">Our Team</div><div class="rule"></div><div class="logo">Kestrel</div>
  <div class="a" style="left:24px;right:24px;top:40px;display:flex;gap:10px">
    <div style="flex:1"><div class="ph" style="position:relative;height:62px;background:linear-gradient(160deg,#cdd5dc,#9aa6b2)" role="img" aria-label="Portrait of team member"></div><div class="center" style="background:var(--navy);color:#fff;font-size:5px;padding:3px">Name Surname</div><div class="tx center" style="margin-top:4px">Lorem ipsum dolor sit amet, consectetur.</div></div>
    <div style="flex:1"><div class="ph" style="position:relative;height:62px;background:linear-gradient(160deg,#cdd5dc,#9aa6b2)" role="img" aria-label="Portrait of team member"></div><div class="center" style="background:var(--navy);color:#fff;font-size:5px;padding:3px">Name Surname</div><div class="tx center" style="margin-top:4px">Lorem ipsum dolor sit amet, consectetur.</div></div>
    <div style="flex:1"><div class="ph" style="position:relative;height:62px;background:linear-gradient(160deg,#cdd5dc,#9aa6b2)" role="img" aria-label="Portrait of team member"></div><div class="center" style="background:var(--navy);color:#fff;font-size:5px;padding:3px">Name Surname</div><div class="tx center" style="margin-top:4px">Lorem ipsum dolor sit amet, consectetur.</div></div>
    <div style="flex:1"><div class="ph" style="position:relative;height:62px;background:linear-gradient(160deg,#cdd5dc,#9aa6b2)" role="img" aria-label="Portrait of team member"></div><div class="center" style="background:var(--navy);color:#fff;font-size:5px;padding:3px">Name Surname</div><div class="tx center" style="margin-top:4px">Lorem ipsum dolor sit amet, consectetur.</div></div></div>
  <div class="foot"><span>© 2025 Kestrel · Business Insight Software</span><b>40</b></div>
</section>

<!-- 41 team with photo -->
<section class="slide">
  <div class="ph" style="left:0;top:0;width:150px;bottom:9px;background:linear-gradient(135deg,#55616d,#c4ccd4 55%,#3b4651)" role="img" aria-label="Photo of a steel bridge structure"></div>
  <div class="a" style="left:0;width:150px;bottom:20px;height:14px;background:var(--navy);color:#fff;font-size:5px;padding:4px 10px">Our Team</div>
  <div class="logo">Kestrel</div>
  <div class="a" style="left:170px;right:16px;top:34px;display:grid;grid-template-columns:1fr 1fr;gap:14px 12px">
    <div class="row" style="align-items:center;grid-column:1/3;justify-content:center"><div class="ph face" style="position:relative;width:28px;height:28px" role="img" aria-label="Portrait of team member"></div><div><div class="h">Name Surname</div><div class="tx">Position Title</div></div></div>
    <div class="row" style="align-items:center"><div class="ph face" style="position:relative;width:28px;height:28px" role="img" aria-label="Portrait of team member"></div><div><div class="h">Name Surname</div><div class="tx">Position Title</div></div></div>
    <div class="row" style="align-items:center"><div class="ph face" style="position:relative;width:28px;height:28px" role="img" aria-label="Portrait of team member"></div><div><div class="h">Name Surname</div><div class="tx">Position Title</div></div></div>
    <div class="row" style="align-items:center;grid-column:1/3;justify-content:center"><div class="ph face" style="position:relative;width:28px;height:28px" role="img" aria-label="Portrait of team member"></div><div><div class="h">Name Surname</div><div class="tx">Position Title</div></div></div></div>
  <div class="foot"><span>© 2025 Kestrel · Business Insight Software</span><b>41</b></div>
</section>

<!-- 42 contact -->
<section class="slide dark">
  <div class="ph" style="inset:0;background:linear-gradient(135deg,#6a7c8e,#b8c4cf 55%,#4a5b6c)" role="img" aria-label="Photo of a glass roof structure"></div>
  <div class="a" style="left:14px;top:10px;width:150px;height:200px;background:rgba(33,58,86,.9);padding:16px 14px">
    <div class="brand" style="color:#fff;font-size:15px">Kestrel</div>
    <div style="color:#fff;font-size:10px;margin:18px 0 10px">Our Contact</div>
    <div class="row" style="align-items:center;margin-bottom:6px"><svg width="8" height="8" viewBox="0 0 10 10"><path d="M5 1a3 3 0 0 1 3 3c0 2.2-3 5-3 5S2 6.2 2 4a3 3 0 0 1 3-3z" fill="#8cc09c"/></svg><span class="tx w">12 Example Street, 1000 Sampletown</span></div>
    <div class="row" style="align-items:center;margin-bottom:6px"><svg width="8" height="8" viewBox="0 0 10 10"><path d="M2 1h2l1 2.5-1.3.8a6 6 0 0 0 2.5 2.5l.8-1.3L9.5 6.5v2a1 1 0 0 1-1 1A8 8 0 0 1 1 2a1 1 0 0 1 1-1z" fill="#8cc09c"/></svg><span class="tx w">+00 123 456 7890</span></div>
    <div class="row" style="align-items:center;margin-bottom:6px"><svg width="8" height="8" viewBox="0 0 10 10"><rect x="1" y="2" width="8" height="6" fill="none" stroke="#8cc09c"/><path d="M1 2l4 3 4-3" fill="none" stroke="#8cc09c"/></svg><span class="tx w">hello@kestrel-example.com</span></div>
    <div class="row" style="align-items:center"><svg width="8" height="8" viewBox="0 0 10 10"><circle cx="5" cy="5" r="4" fill="none" stroke="#8cc09c"/><path d="M1 5h8M5 1c2 2.5 2 5.5 0 8M5 1c-2 2.5-2 5.5 0 8" fill="none" stroke="#8cc09c" stroke-width=".8"/></svg><span class="tx w">www.kestrel-example.com</span></div>
    <div style="display:flex;gap:4px;margin-top:16px"><span style="width:8px;height:8px;border-radius:50%;background:var(--green)"></span><span style="width:8px;height:8px;border-radius:50%;background:var(--green)"></span><span style="width:8px;height:8px;border-radius:50%;background:var(--green)"></span></div>
  </div>
  <div class="a" style="right:28px;top:118px;color:#fff;font-size:16px;font-weight:700;letter-spacing:.5px">THANK YOU</div>
  <div class="a tx w" style="right:28px;top:140px">For your attention</div>
</section>

</main>
</body>
</html>
```